Design refresh of existing HR Application

Talvora is an HR & Payroll processing software, already in use by thousands of people. It is a feature packed, enterprise-grade software that is also simple and user friendly. Visit us at https://talvora.example

Seeking a refresh of the app design/UI.

Key objectives are to make it "sleeker", more professional and polished, whist still retaining functionality. Not intended to be a massive overhaul, but more of reorganization and improvements on design elements.

You may login to our demo account to see the app live.
https://app.talvora.example/login
User: demo@talvora.example
Password: Bex47

Target Market(s)

HR Managers, business administrators/owners and employees.

Industry/Entity Type

Business Software

Number of Pages Required

4 page

Font styles to use
Other font styles liked:
• Lato

Colors
0255a3
3377b5
00a990
33b8a4
f37122
faa54b

Requirements
Must have
• Must retain the current functionality on each page.
Nice to have
• Fine to suggest changes to colors, font sizes, card designs, moving sections around and any other design element changes.

```html
<!DOCTYPE html>
<html lang="en">
<head>
<meta charset="utf-8">
<title>Talvora – Dashboard</title>
<link href="https://fonts.googleapis.com/css2?family=Poppins:wght@300;400;500;600;700&display=swap" rel="stylesheet">
<style>
:root{
  --sidebar:#3e3f97;
  --sidebar-line:#5a5bab;
  --bg:#f2f3f8;
  --card:#ffffff;
  --ink:#1f1f2e;
  --muted:#5c5c6a;
  --line:#e3e4ea;
  --orange:#f37122;
  --orange-soft:#fde4d3;
  --navy:#0255a3;
  --blue-soft:#dde8f5;
  --teal:#00a990;
  --teal-mid:#1ba58f;
  --sky:#19b6e6;
}
*{box-sizing:border-box;margin:0;padding:0}
html,body{width:1200px;height:844px;overflow:hidden}
body{font-family:"Poppins",sans-serif;background:var(--bg);color:var(--ink);position:relative}

.sidebar{position:absolute;left:0;top:0;width:220px;height:844px;background:var(--sidebar);color:#fff}
.brand{position:absolute;top:22px;left:0;width:220px;text-align:center}
.brand-mark{width:34px;height:34px;border-radius:50%;background:#fff;margin:0 auto 8px}
.brand-name{font-size:11px;font-weight:600;letter-spacing:1px}
.nav{position:absolute;top:124px;left:22px;width:175px;list-style:none}
.nav li{height:51px;display:flex;align-items:center;gap:12px;font-size:15px;border-bottom:1px solid var(--sidebar-line)}
.nav li:last-child{border-bottom:none}
.nav li.active{background:var(--orange);border-radius:21px;height:41px;padding-left:28px;border:none;margin-bottom:5px}
.nav svg{width:26px;height:26px;flex:none}

.topbar{position:absolute;left:220px;top:0;width:980px;height:89px;background:#fff;display:flex;align-items:center}
.company{margin-left:25px;font-size:15px;font-weight:500;letter-spacing:.3px;width:475px}
.company span{font-size:10px;margin-left:8px}
.sep{width:1px;height:46px;background:var(--line)}
.lang{width:112px;text-align:center;font-size:15px}
.help{width:76px;display:flex;justify-content:center}
.user{display:flex;align-items:center;gap:10px;padding-left:28px;width:233px}
.avatar{width:47px;height:47px;border-radius:50%;background:linear-gradient(135deg,#3aa24a,#7a5a3e)}
.user-name{font-size:16px;font-weight:600;letter-spacing:.5px}
.user-role{font-size:12.5px;color:var(--muted)}
.caret{width:30px;display:flex;justify-content:center}

.card{position:absolute;background:var(--card);border-radius:3px}
.card-title{display:flex;align-items:center;gap:9px;font-size:15.5px;font-weight:600;letter-spacing:.5px;padding:14px 0 10px;margin:0 20px;border-bottom:1px solid var(--line)}
.card-title svg{width:19px;height:19px}

.event{left:246px;top:142px;width:217px;height:249px;text-align:center}
.event-date{font-size:11px;margin-top:12px;color:var(--muted)}
.pills{display:flex;justify-content:center;gap:4px;margin-top:5px}
.pill{background:#ececef;border-radius:15px;padding:3px 14px;font-size:16px;font-weight:600}
.ring{position:absolute;left:63px;top:124px}
.ring-text{position:absolute;left:0;top:161px;width:217px;text-align:center;font-size:11px;color:var(--muted)}
.ring-time{position:absolute;left:0;top:174px;width:217px;text-align:center;font-size:22px;font-weight:600;color:var(--teal)}
.event-branch{position:absolute;left:0;top:225px;width:217px;font-size:11.5px;color:var(--muted)}

.schedule{left:472px;top:142px;width:479px;height:249px}
.schedule .card-title{margin-right:258px}
.month-nav{position:absolute;left:274px;top:14px;width:192px;display:flex;justify-content:space-between;align-items:center;font-size:14px;letter-spacing:.5px}
.month-nav b{width:24px;height:24px;border-radius:50%;background:#ececef;display:flex;align-items:center;justify-content:center;font-weight:500;font-size:13px}
.sched-list{position:absolute;left:15px;top:62px;width:230px}
.sched-row{display:grid;grid-template-columns:36px 40px 1fr;height:56px;font-size:12.5px;border-bottom:1px solid var(--line);margin-bottom:8px}
.sched-row:last-child{border:none}
.sched-row .day{font-weight:600;font-size:12.5px;padding-top:8px}
.sched-row .date{line-height:13px;font-size:12.5px;border-right:1px solid var(--line);padding-top:4px}
.sched-row .items{padding-left:14px;line-height:16px;color:var(--muted);font-weight:300;padding-top:2px}
.cal{position:absolute;left:270px;top:64px;display:grid;grid-template-columns:repeat(7,28.5px);grid-template-rows:20px 22px repeat(5,27px)}
.cal span{display:flex;align-items:center;justify-content:center;font-size:12.5px}
.cal .h{color:#8a8a96;font-size:11.5px}

.timeoff{left:961px;top:142px;width:217px;height:249px}
.leave{position:absolute;top:62px;width:104px;text-align:center}
.leave .circ{width:76px;height:76px;border-radius:50%;margin:0 auto 14px;display:flex;align-items:center;justify-content:center}
.leave .t{font-size:12px;font-weight:600;letter-spacing:.3px}
.leave .s{font-size:12px;color:var(--muted)}
.request{position:absolute;left:16px;top:190px;width:184px;height:41px;border-radius:21px;background:var(--teal-mid);color:#fff;font-weight:600;font-size:14px;letter-spacing:.5px;display:flex;align-items:center;justify-content:center}

.section-title{position:absolute;left:246px;top:442px;font-size:15.5px;font-weight:600;letter-spacing:.7px}
.tile{position:absolute;top:471px;width:225px;height:68px;background:#fff;border-radius:3px;display:flex;align-items:center}
.tile .num{font-size:36px;font-weight:600;margin-left:23px;width:41px;letter-spacing:-1px}
.tile .lbl{font-size:12.5px;line-height:13px;margin-left:6px;flex:1}
.tile .ico{width:54px;height:54px;margin-right:8px;display:flex;align-items:center;justify-content:center}

.notes{left:248px;top:591px;width:517px;height:219px}
.announce{left:772px;top:591px;width:406px;height:219px}
.panel-head{display:flex;justify-content:space-between;align-items:center;margin:0 18px;padding:12px 0 14px;border-bottom:1px solid var(--line)}
.panel-head h2{font-size:15.5px;font-weight:600;letter-spacing:.5px}
.starred{font-size:13px;color:var(--muted);display:flex;align-items:center;gap:6px}
.note-list{list-style:none;margin:14px 40px 0 18px}
.note-list li{display:flex;align-items:center;gap:7px;font-size:12px;color:var(--muted);height:35.5px;border-bottom:1px solid #efeff3;position:relative;white-space:nowrap}
.note-list li:last-child{border:none}
.note-list li::after,.ann-list li::after{content:"‹";position:absolute;right:-24px;top:4px;font-size:18px;color:var(--ink)}
.ann-list{list-style:none;margin:22px 76px 0 20px}
.ann-list li{font-size:12px;color:var(--muted);line-height:18px;padding-bottom:14px;margin-bottom:12px;border-bottom:1px solid #efeff3;position:relative}
.ann-list li::after{right:-32px;top:-4px}
.ann-list li:last-child{border:none}
.scroll{position:absolute;width:3px;background:#e6e6ec;border-radius:2px}
</style>
</head>
<body>
<svg width="0" height="0" style="position:absolute">
  <symbol id="cal-clock" viewBox="0 0 32 32"><rect x="2" y="5" width="22" height="20" rx="2" fill="none" stroke="currentColor" stroke-width="2"/><path d="M2 11h22M8 2v6M18 2v6" stroke="currentColor" stroke-width="2"/><rect x="6" y="14" width="3" height="3" fill="currentColor"/><rect x="11" y="14" width="3" height="3" fill="currentColor"/><rect x="6" y="19" width="3" height="3" fill="currentColor"/><circle cx="24" cy="24" r="6.5" fill="#fff" stroke="currentColor" stroke-width="2"/><path d="M24 20.5v4h3" stroke="currentColor" stroke-width="1.8" fill="none"/></symbol>
  <symbol id="cal" viewBox="0 0 20 20"><rect x="1" y="3" width="18" height="16" rx="1" fill="none" stroke="currentColor" stroke-width="1.5"/><path d="M1 8h18M6 1v4M14 1v4M5 11h2M9 11h2M13 11h2M5 15h2M9 15h2M13 15h2" stroke="currentColor" stroke-width="1.5"/></symbol>
  <symbol id="star" viewBox="0 0 20 20"><path d="M10 1l2.8 5.8 6.2.9-4.5 4.4 1.1 6.3L10 15.4 4.4 18.4l1.1-6.3L1 7.7l6.2-.9z" fill="currentColor"/></symbol>
</svg>

<aside class="sidebar">
  <div class="brand"><div class="brand-mark"></div><div class="brand-name">TALVORA</div></div>
  <ul class="nav">
    <li class="active"><svg viewBox="0 0 26 26"><path d="M2 19a11 11 0 0 1 22 0z" fill="#fff"/><circle cx="13" cy="17" r="2" fill="#f37122"/></svg>Dashboard</li>
    <li><svg viewBox="0 0 26 26" fill="#fff"><circle cx="10" cy="8" r="4.5"/><path d="M2 22a8 8 0 0 1 16 0z"/><circle cx="19" cy="9" r="3"/><path d="M17 14a6 6 0 0 1 8 6h-6z"/></svg>Employees</li>
    <li><svg viewBox="0 0 20 20" style="color:#fff"><use href="#cal"/></svg>Calendar</li>
    <li><svg viewBox="0 0 26 26"><rect x="3" y="2" width="15" height="21" rx="2" fill="#fff"/><circle cx="18" cy="18" r="6" fill="#fff" stroke="#3e3f97" stroke-width="1.5"/><text x="15.5" y="21.5" font-size="9" fill="#3e3f97" font-family="Poppins">$</text></svg>Expenses</li>
    <li><svg viewBox="0 0 26 26"><rect x="3" y="3" width="17" height="20" rx="2" fill="#fff"/><path d="M6 8h11M6 12h11M6 16h7" stroke="#3e3f97" stroke-width="1.5"/><circle cx="20" cy="19" r="5" fill="#fff" stroke="#3e3f97" stroke-width="1.5"/></svg>Payroll</li>
    <li><svg viewBox="0 0 26 26" fill="#fff"><rect x="2" y="15" width="4" height="9"/><rect x="8" y="11" width="4" height="13"/><rect x="14" y="13" width="4" height="11"/><rect x="20" y="7" width="4" height="17"/><path d="M3 11l6-5 5 3 9-7" stroke="#fff" stroke-width="2" fill="none"/></svg>Performance</li>
    <li><svg viewBox="0 0 26 26" fill="none" stroke="#fff" stroke-width="2.2"><circle cx="12" cy="14" r="10"/><circle cx="12" cy="14" r="5"/><path d="M12 14L23 3"/></svg>Engagement</li>
    <li><svg viewBox="0 0 26 26"><path d="M5 2h11l6 6v16H5z" fill="#fff"/><circle cx="13" cy="16" r="4.5" fill="#3e3f97"/></svg>Reports</li>
    <li><svg viewBox="0 0 26 26"><circle cx="13" cy="13" r="9" fill="none" stroke="#fff" stroke-width="5" stroke-dasharray="4 3"/><circle cx="13" cy="13" r="6" fill="#fff"/><circle cx="13" cy="13" r="3" fill="#3e3f97"/></svg>Settings</li>
  </ul>
</aside>

<header class="topbar">
  <div class="company">PT TALVORA MANUFACTURING (DEMO)<span>⌄</span></div>
  <div class="sep"></div>
  <div class="lang">English <small>⌄</small></div>
  <div class="sep"></div>
  <div class="help"><svg width="24" height="24" viewBox="0 0 24 24"><circle cx="12" cy="12" r="10.5" fill="none" stroke="#1f1f2e" stroke-width="1.6"/><text x="8" y="17" font-size="13" font-family="Poppins" font-weight="500">?</text></svg></div>
  <div class="sep"></div>
  <div class="user"><div class="avatar" role="img" aria-label="Profile photo of the signed-in user"></div><div><div class="user-name">RENATA SOLBERG</div><div class="user-role">HR Administrator</div></div></div>
  <div class="sep"></div>
  <div class="caret"><svg width="12" height="8" viewBox="0 0 12 8"><path d="M1 1l5 5 5-5" stroke="#1f1f2e" stroke-width="1.8" fill="none"/></svg></div>
</header>

<section class="card event">
  <div class="card-title"><svg style="color:#c9c9d1"><use href="#cal"/></svg>TODAYS EVENT</div>
  <div class="event-date">TUE 26 MAY 20</div>
  <div class="pills"><span class="pill">09:00</span><span class="pill">19:00</span></div>
  <svg class="ring" width="92" height="92" viewBox="0 0 92 92"><circle cx="46" cy="46" r="42" fill="none" stroke="#dfeeea" stroke-width="4"/><circle cx="46" cy="46" r="42" fill="none" stroke="#00a990" stroke-width="4" stroke-dasharray="210 264" transform="rotate(-60 46 46)"/></svg>
  <div class="ring-text">CHECKED IN</div>
  <div class="ring-time">08:50</div>
  <div class="event-branch">WORKING BRANCH B</div>
</section>

<section class="card schedule">
  <div class="card-title"><svg style="color:#c9c9d1"><use href="#cal"/></svg>MY SCHEDULE</div>
  <div class="month-nav"><b>‹</b>MAY<b>›</b></div>
  <div class="sched-list">
    <div class="sched-row"><div class="day">TUE</div><div class="date">MAY<br>20</div><div class="items">09:00 Working<br>18:00 Branch B</div></div>
    <div class="sched-row"><div class="day">THU</div><div class="date">MAY<br>28</div><div class="items">10:00 Working Project A<br>12:00 Branch A</div></div>
  </div>
  <div class="cal">
    <span class="h">M</span><span class="h">T</span><span class="h">W</span><span class="h">T</span><span class="h">F</span><span class="h">S</span><span class="h">S</span>
    <span></span><span></span><span></span><span></span><span></span><span></span><span>1</span>
    <span>2</span><span>3</span><span>4</span><span>5</span><span>6</span><span>7</span><span>8</span>
    <span>9</span><span>10</span><span>11</span><span>12</span><span>13</span><span>14</span><span>15</span>
    <span>16</span><span>17</span><span>18</span><span>19</span><span>20</span><span>21</span><span>22</span>
    <span>23</span><span>24</span><span>25</span><span>26</span><span>27</span><span>28</span><span>29</span>
    <span>31</span>
  </div>
</section>

<section class="card timeoff">
  <div class="card-title"><svg viewBox="0 0 20 20"><circle cx="10" cy="10" r="9" fill="#dcdce2"/><path d="M10 5v5h4" stroke="#fff" stroke-width="1.6" fill="none"/></svg>MY TIME OFF</div>
  <div class="leave" style="left:8px"><div class="circ" style="background:var(--blue-soft);color:var(--navy)"><svg width="42" height="42"><use href="#cal-clock"/></svg></div><div class="t">ANNUAL LEAVE</div><div class="s">6 Left</div></div>
  <div class="leave" style="left:112px"><div class="circ" style="background:var(--orange-soft);color:var(--orange)"><svg width="42" height="42"><use href="#cal-clock"/></svg></div><div class="t">SICK DAYS</div><div class="s">1 Taken</div></div>
  <div class="request">REQUEST</div>
</section>

<h2 class="section-title">QUICK LINKS</h2>
<div class="tile" style="left:246px"><span class="num" style="color:var(--navy)">12</span><span class="lbl">EVENT<br>AMENDMENT</span><span class="ico" style="background:var(--navy);color:#fff"><svg width="34" height="34"><use href="#cal-clock"/></svg></span></div>
<div class="tile" style="left:482px"><span class="num" style="color:var(--teal)">03</span><span class="lbl">LEAVE<br>REQUESTS</span><span class="ico" style="background:var(--teal-mid);color:#fff"><svg width="34" height="34"><use href="#cal-clock"/></svg></span></div>
<div class="tile" style="left:717px"><span class="num" style="color:var(--orange)">07</span><span class="lbl">EVENT<br>REQUESTS</span><span class="ico" style="background:var(--orange);color:#fff"><svg width="34" height="34"><use href="#cal-clock"/></svg></span></div>
<div class="tile" style="left:953px"><span class="num" style="color:var(--sky)">02</span><span class="lbl">PAYROLLS<br>PENDING</span><span class="ico" style="background:var(--sky)"><svg width="34" height="34" viewBox="0 0 26 26"><rect x="4" y="4" width="15" height="18" rx="2" fill="#fff"/><path d="M7 9h9M7 13h9M7 17h5" stroke="#19b6e6" stroke-width="1.5"/><circle cx="19" cy="19" r="5" fill="#fff" stroke="#19b6e6" stroke-width="1.5"/></svg></span></div>

<section class="card notes">
  <div class="panel-head"><h2>NOTIFICATIONS</h2><span class="starred"><svg width="17" height="17" style="color:var(--orange)"><use href="#star"/></svg>View Starred</span></div>
  <ul class="note-list">
    <li><svg width="13" height="13" style="color:#b4b4bd"><use href="#cal"/></svg>Wirawan, Sekar requests Annual Leave on 11 Jun 2020.</li>
    <li><svg width="13" height="13" style="color:#b4b4bd"><use href="#cal"/></svg>Wirawan, Sekar has remotely checked in for Working on 20/05/2020 02:07</li>
    <li><svg width="13" height="13" style="color:#b4b4bd"><use href="#cal"/></svg>Wirawan, Sekar requests amendment on 15 Apr 2020 from 09:00 - 18:00.</li>
    <li><svg width="13" height="13" style="color:#b4b4bd"><use href="#cal"/></svg>Overtime request for Wirawan, Sekar - 18 May 2020 at 19:00 | 21:00 Branch A</li>
  </ul>
  <div class="scroll" style="left:506px;top:98px;height:66px"></div>
</section>

<section class="card announce">
  <div class="panel-head"><h2>ANNOUNCEMENTS</h2><span class="starred"><svg width="17" height="17" style="color:var(--orange)"><use href="#star"/></svg>View Starred</span></div>
  <ul class="ann-list">
    <li>Please be reminded that walking on factory floor without helmet will result in a Rp500,000 fine. Be safe!</li>
    <li>Free Friday drinks are available in the pantry on every week until the end of this year. Take the opportunity to get to know more people!</li>
  </ul>
  <div class="scroll" style="left:391px;top:66px;height:57px"></div>
</section>
</body>
</html>
```